WHAT LIES BEYOND? Discovering the shape of days with the Silent Lamp

Creating a book that is about living a spiritual life. The book is about letting go of the materialistic world and finding happiness through self realisation and enlightenment. The contents page is below that gives an idea of what is contained in the book.

The book is based on the writings of the Sikhs - from India. But it is written in a universal way that is understandable to all.

CONTENTS
Living for a purpose
- Born to be original! Dying as a copy!
- My relationship with everything but me!
- What is my purpose?

Life as a human being!
- Stages of Life
- Five Weaknesses

What is driving our lives?
- Information overload?
- What are your drivers?
- Giving life meaning

You reap what you sow
- Is my destiny written?
- Good and bad actions
- Maya – the illusion and it’s three modes

Slow down and let go
- The mind in overdrive
- Being aware of our mental health
- Why Slow Down?

The Guidance of the Guru
- Why do I need a Guru?
- What the Guru gives you
- Gurbani – the Guru’s Words

Staying connected
- Repeating the Mantra
- Doing two things at once
- Remembering in times of difficulty

Cultivating virtues
- Theory vs Practice
- Virtues and true religion
- Some key virtues

The Mystical Creation
- Experiencing ecstasy
- Enlightenment and intuition
- Spiritual Transformation

Good Company
- How do my companions affect me?
- The company of Saintly people
- Obtaining the fruits that the Guru describes

Serving selflessly
- Serving is our purpose
- Being grateful
- Being generous

Ten things to change your life today

Target Market(s)

All those who want to learn about spirituality. We are targeting young and middle aged but not necessarily ruling out older demographic.

Requirements
Must have
• The book cover:

- exciting and intriguing
- theme is "what lies beyond" in this world
- some kind of lean towards enlightenment
Nice to have
• It is not essential but the cover could subtly show something about the Sikh faith. Can discuss this further if necessary.
Should not have
• Should not:

- look dull and boring
- don't want it to look like a Buddhism book

```html
<!DOCTYPE html>
<html lang="en">
<head>
<meta charset="utf-8">
<title>What Lies Beyond? – Book Cover</title>
<link rel="stylesheet" href="https://fonts.googleapis.com/css2?family=Libre+Baskerville:wght@700&family=Open+Sans:wght@400&display=swap">
<style>
  :root {
    --sky-dark: #2a2927;
    --sky-grey: #77746b;
    --haze-amber: #c89a4e;
    --glow-light: #fff4c8;
    --ground-dark: #1b1209;
    --title-red: #b0220f;
    --title-red-deep: #6e0f05;
    --title-edge: #3a0802;
    --cream-text: #f3e9ad;
  }
  * { margin: 0; padding: 0; box-sizing: border-box; }
  html, body {
    width: 788px;
    height: 1200px;
    overflow: hidden;
    background: #ffffff;
  }
  .book-cover {
    position: relative;
    width: 788px;
    height: 1200px;
    overflow: hidden;
  }
  .cover-scene {
    position: absolute;
    inset: 0;
    background:
      radial-gradient(ellipse 240px 300px at 50% 47%, var(--glow-light) 0%, rgba(255,228,150,0.75) 35%, rgba(230,170,80,0) 100%),
      linear-gradient(to bottom,
        var(--sky-dark) 0%,
        var(--sky-grey) 16%,
        #a99a78 32%,
        var(--haze-amber) 55%,
        #b17a2d 72%,
        #5c3a14 86%,
        var(--ground-dark) 100%);
  }
  .cover-scene::after {
    content: "";
    position: absolute;
    inset: 0;
    background: linear-gradient(to right, rgba(0,0,0,0.35) 0%, rgba(0,0,0,0) 14%, rgba(0,0,0,0) 86%, rgba(0,0,0,0.35) 100%);
  }
  .tagline {
    position: absolute;
    top: 40px;
    left: 0;
    right: 0;
    text-align: center;
    font-family: "Open Sans", sans-serif;
    font-size: 30px;
    color: var(--cream-text);
    letter-spacing: 0.3px;
  }
  .title {
    position: absolute;
    top: 330px;
    left: 0;
    right: 0;
    text-align: center;
    font-family: "Libre Baskerville", serif;
    font-weight: 700;
    font-size: 104px;
    line-height: 148px;
    color: var(--title-red);
    background: linear-gradient(to bottom, #d2361c 0%, var(--title-red) 45%, var(--title-red-deep) 100%);
    -webkit-background-clip: text;
    background-clip: text;
    -webkit-text-fill-color: transparent;
    -webkit-text-stroke: 1.5px var(--title-edge);
    filter: drop-shadow(1px 2px 1px rgba(40,10,0,0.55));
  }
  .title span { display: block; }
  .subtitle {
    position: absolute;
    top: 1005px;
    left: 0;
    right: 0;
    text-align: center;
    font-family: "Open Sans", sans-serif;
    font-size: 40px;
    line-height: 58px;
    color: var(--cream-text);
  }
</style>
</head>
<body>
  <main class="book-cover">
    <div class="cover-scene" role="img" aria-label="Photograph of a bare tree silhouetted against a glowing sunrise in golden mist"></div>
    <p class="tagline">Ten things to change your life today</p>
    <h1 class="title">
      <span>WHAT</span>
      <span>LIES</span>
      <span>BEYOND?</span>
    </h1>
    <p class="subtitle">Discovering the shape of days<br>with the Silent Lamp</p>
  </main>
</body>
</html>
```